Simple, elegant, business card design required

Hi designers,I am looking for a simple yet elegant business card design.

Please make use of my logo (attached); you are free to tweak the logo should you wish to do so.

Our business is involved in many different fields - almost all of them involved in some form of "design", so that's really one of the key things I want to portray. I do not wish to specify which field of design, exactly.

I prefer white on black (or just monochromatic), but if you have a different, creative idea, I am open to that too.

You can use artsy photographs provided that you have the license to use those. Please feel free to ask me any questions.
Updates

Project Deadline Extended Reason: Small extension for potential revisions. Did not get the time to provide as much feedback as I can. Added Wednesday, July 09, 2014

Target Market(s)

High-end customers looking for design consultancy

Industry/Entity Type

Business

Contact Information for Business Card

Name: Gareth Moonfield
Position: Creative Director
Mobile: +155603928174
Address: Barrow Lane, Elmbridge upon Wyle, Dunmoreshire GL12 4RT
Website: torvakest.com (not launched yet)

Requirements
Must have
• Design layout must be clean, original, and text must be readable when printed.
Should not have
• ~ No business card templates please. Anyone using this will be reported.
• ~ Please don't spam entries.

```html
<!DOCTYPE html>
<html lang="en">
<head>
<meta charset="utf-8">
<title>Torvakest — Business Card</title>
<link rel="stylesheet" href="https://fonts.googleapis.com/css2?family=Jost:wght@400;500;600&display=swap">
<style>
  :root {
    --ink: #0d0d0d;
    --paper: #f4f4f2;
    --backdrop: #d9d9d6;
    --muted: #3a3a3a;
  }
  * { margin: 0; padding: 0; box-sizing: border-box; }
  html, body {
    width: 1200px; height: 900px; overflow: hidden;
    background: var(--backdrop);
    font-family: "Jost", "Futura", sans-serif;
    color: var(--ink);
  }
  .sheet {
    width: 1200px; height: 900px;
    display: flex; flex-direction: column;
    align-items: center; justify-content: center;
    gap: 40px;
  }
  .card {
    position: relative;
    width: 700px; height: 400px;
    background: var(--paper);
    overflow: hidden;
    box-shadow: 0 6px 18px rgba(0,0,0,0.15);
  }

  /* Front */
  .front__band {
    position: absolute; left: 0; top: 0;
    width: 190px; height: 100%;
    background: var(--ink);
    display: flex; align-items: flex-start; justify-content: center;
    padding-top: 92px;
  }
  .front__mark {
    width: 46px; height: 46px;
    border: 4px solid var(--paper);
    border-radius: 50%;
  }
  .front__name {
    position: absolute; left: 228px; top: 128px;
    font-size: 44px; font-weight: 500;
    letter-spacing: 0.42em;
    line-height: 1;
    white-space: nowrap;
  }

  /* Back */
  .back__block {
    position: absolute; left: 0; top: 0;
    width: 320px; height: 200px;
    background: var(--ink);
    display: flex; align-items: center; justify-content: flex-end;
    padding-right: 34px;
  }
  .back__mark {
    width: 150px; height: 150px;
    border: 26px solid var(--paper);
    border-radius: 50%;
  }
  .back__details {
    position: absolute; right: 54px; top: 150px;
    text-align: right;
    text-transform: uppercase;
    letter-spacing: 0.2em;
    white-space: nowrap;
  }
  .person__name {
    font-size: 15px; font-weight: 600;
    letter-spacing: 0.24em;
  }
  .person__role {
    font-size: 10px; font-weight: 400;
    color: var(--muted);
    margin-top: 6px;
  }
  .address {
    margin-top: 24px;
    font-size: 12px; line-height: 1.7;
    font-style: normal;
  }
  .contact {
    margin-top: 12px;
    font-size: 12px; line-height: 1.9;
  }
  .contact__line {
    display: flex; align-items: center; justify-content: flex-end; gap: 12px;
  }
  .contact__icon { width: 13px; height: 15px; }
</style>
</head>
<body>
<main class="sheet">

  <section class="card front" aria-label="Card front">
    <div class="front__band">
      <span class="front__mark"></span>
    </div>
    <h1 class="front__name">TORVAKEST</h1>
  </section>

  <section class="card back" aria-label="Card back">
    <div class="back__block">
      <span class="back__mark"></span>
    </div>
    <div class="back__details">
      <p class="person__name">Gareth Moonfield</p>
      <p class="person__role">Creative Director</p>
      <address class="address">
        Barrow Lane<br>
        Elmbridge upon Wyle<br>
        Dunmoreshire GL12 4RT
      </address>
      <div class="contact">
        <p class="contact__line">+155603928174
          <svg class="contact__icon" viewBox="0 0 13 15" aria-hidden="true">
            <rect x="2" y="0.8" width="9" height="13.4" rx="1.5" fill="none" stroke="#0d0d0d" stroke-width="1.3"/>
            <line x1="5" y1="12" x2="8" y2="12" stroke="#0d0d0d" stroke-width="1.2"/>
          </svg>
        </p>
        <p class="contact__line">Website: torvakest.com
          <svg class="contact__icon" viewBox="0 0 15 15" aria-hidden="true">
            <circle cx="7.5" cy="7.5" r="6.4" fill="none" stroke="#0d0d0d" stroke-width="1.3"/>
            <ellipse cx="7.5" cy="7.5" rx="2.8" ry="6.4" fill="none" stroke="#0d0d0d" stroke-width="1"/>
            <line x1="1.1" y1="7.5" x2="13.9" y2="7.5" stroke="#0d0d0d" stroke-width="1"/>
          </svg>
        </p>
      </div>
    </div>
  </section>

</main>
</body>
</html>
```